Need a business card for a Construction and Remodeling company.
Our company logo is the fleur de lis design as thats the family crust that we use on our logos.
Heres the info it needs:

Brackmore Construction & Remodeling, LLC
Renovations * Restorations

Elwin R. Brackmore
845 North Quarry Road
Ashbury Connecticut 06099
(203) 555.0182
CT LIC/REG: 418257

home owners, customers

```html
<!DOCTYPE html>
<html lang="en">
<head>
<meta charset="utf-8">
<title>Brackmore Construction &amp; Remodeling — Business Card</title>
<link href="https://fonts.googleapis.com/css2?family=Archivo+Black&family=Dancing+Script:wght@500&family=Roboto:wght@400;500&display=swap" rel="stylesheet">
<style>
  :root {
    --stage: #232323;
    --card-white: #ffffff;
    --card-black: #151515;
    --ink: #111111;
    --brand-red: #e4222b;
    --accent-green: #8cc63f;
    --crest-grey: #e8e8e8;
    --silver: #b9b9b9;
    --muted: #333333;
  }
  * { margin: 0; padding: 0; box-sizing: border-box; }
  html, body { width: 1200px; height: 1200px; overflow: hidden; background: var(--stage); }
  .stage {
    width: 1200px; height: 1200px;
    display: flex; flex-direction: column; align-items: center; justify-content: center; gap: 40px;
  }
  .card {
    position: relative; width: 900px; height: 514px; border-radius: 22px; overflow: hidden;
  }
  .card--back { background: var(--card-black); display: flex; align-items: center; justify-content: center; }
  .card--front { background: var(--card-white); }

  .lockup { display: flex; align-items: center; gap: 22px; position: relative; z-index: 1; }
  .lockup__circle { width: 96px; height: 96px; border-radius: 50%; border: 9px solid var(--brand-red); flex: none; }
  .lockup__name {
    font-family: "Archivo Black", sans-serif; color: var(--ink);
    font-size: 30px; line-height: 1.1; letter-spacing: 0.5px; text-transform: uppercase;
  }
  .lockup__tagline {
    font-family: "Dancing Script", cursive; font-size: 22px; color: var(--muted);
    margin-top: 6px;
  }
  .lockup__tagline .dot { color: var(--accent-green); padding: 0 10px; font-family: "Roboto", sans-serif; font-size: 16px; }

  .card--back .lockup__circle { border-color: var(--silver); }
  .card--back .lockup__name { color: var(--silver); }
  .card--back .lockup__tagline { color: #8a8a8a; }

  .card--front .lockup { position: absolute; left: 70px; top: 60px; }

  .contact { position: absolute; left: 80px; top: 290px; font-family: "Roboto", sans-serif; color: var(--ink); z-index: 1; }
  .contact__name { font-family: "Archivo Black", sans-serif; font-size: 26px; letter-spacing: 1px; text-transform: uppercase; }
  .contact__phone { display: flex; align-items: center; gap: 10px; font-size: 24px; font-weight: 500; margin: 6px 0 10px; }
  .contact__phone svg { width: 22px; height: 22px; fill: var(--brand-red); }
  .contact__line { font-size: 19px; line-height: 1.35; }

  .crest-watermark {
    position: absolute; right: 30px; top: 200px; width: 290px; height: 314px;
    border-radius: 145px 145px 30px 30px;
    background: radial-gradient(ellipse at 50% 45%, var(--crest-grey) 0%, rgba(232,232,232,0.5) 60%, rgba(255,255,255,0) 100%);
  }
</style>
</head>
<body>
<main class="stage">
  <section class="card card--back" aria-label="Card back">
    <div class="lockup">
      <span class="lockup__circle"></span>
      <div>
        <p class="lockup__name">Brackmore<br>Construction &amp; Remodeling, LLC</p>
        <p class="lockup__tagline">Renovations<span class="dot">•</span>Additions<span class="dot">•</span>Restorations</p>
      </div>
    </div>
  </section>

  <section class="card card--front" aria-label="Card front">
    <div class="crest-watermark" role="img" aria-label="Faint family crest watermark"></div>
    <div class="lockup">
      <span class="lockup__circle"></span>
      <div>
        <p class="lockup__name">Brackmore<br>Construction &amp; Remodeling, LLC</p>
        <p class="lockup__tagline">Renovations<span class="dot">•</span>Additions<span class="dot">•</span>Restorations</p>
      </div>
    </div>
    <div class="contact">
      <p class="contact__name">Elwin R. Brackmore</p>
      <p class="contact__phone">
        <svg viewBox="0 0 24 24" aria-hidden="true"><path d="M6.6 10.8a15.1 15.1 0 0 0 6.6 6.6l2.2-2.2a1 1 0 0 1 1-.25 11.4 11.4 0 0 0 3.6.57 1 1 0 0 1 1 1V20a1 1 0 0 1-1 1A17 17 0 0 1 3 4a1 1 0 0 1 1-1h3.5a1 1 0 0 1 1 1c0 1.25.2 2.45.57 3.57a1 1 0 0 1-.25 1z"/></svg>
        (203) 555-0182
      </p>
      <p class="contact__line">LIC/REG: 418257</p>
      <p class="contact__line">845 North Quarry Road</p>
      <p class="contact__line">Ashbury Connecticut 06099</p>
    </div>
  </section>
</main>
</body>
</html>
```